Maelis Spacial\floral Decorator

Maelis is a spacial\floral decorator. She is passionate about Art, Life, Architecture, Painting, Music and movement. Her website will be used to showcase her spacial and floral design projects.
We are looking for a very unique website that stands apart from the crowd.
We believe that is achieved through simple high quality design Simple being very important.
The Home page should display primarily photos.
Your task is to provide an un-coded homepage template.
The page must be dynamic in its style and feel.

Maelis has suggest a grid pattern for the images, similar to this http://www.dorvanbloomhouse.co.uk. Overall We like the look and feel of this site.

We like the following color palettes, please base your design around one of them;
https://tintrova.example.com/#themes/search?term=5531704
https://tintrova.example.com/#themes/search?term=5536218
https://tintrova.example.com/#themes/search?term=5548126
https://tintrova.example.com/#themes/search?term=5540967
https://tintrova.example.com/#themes/search?term=5537419

Our target Market is High End Corporate Clients, located in Shanghai and Taipai. For these clients she utilise her floral and interior design skills to decorate a space. See Photos 2, 3 and 21 for examples.
She also targets High End personal clients for events such as weddings and gift combination i.e. flowers and something else.

Requirements
Must have
• Chinese/ English Language Selection
A selection of pictures that appear and disappear.
A menu system that includes:
Home – Portfolio – About Maelis – Blog – Contact Her
A very subtle menu system linking to chatnest, worklinq On, v+ and xunmo.
Nice to have
• We also like the use of an image for the background but this is not necessary.
Should not have
• Alot of Text, yes we now this isn't great for SEO but we will deal with that on other pages

```html
<!DOCTYPE html>
<html lang="en">
<head>
<meta charset="utf-8">
<title>About Maelis – Maelis's Spacial Design</title>
<link href="https://fonts.googleapis.com/css2?family=Arimo:wght@400;700&family=Dancing+Script:wght@600&display=swap" rel="stylesheet">
<style>
  :root {
    --sidebar-bg: #f2efe2;
    --plum-dark: #221427;
    --plum: #44345a;
    --slate: #67708f;
    --sage: #94bda4;
    --cream: #fffde5;
    --ink: #111111;
    --muted-ink: #4a4a4a;
    --panel-bg: rgba(255, 255, 255, 0.58);
    --panel-border: #ffffff;
  }
  * { box-sizing: border-box; margin: 0; padding: 0; }
  html, body { width: 1200px; height: 675px; overflow: hidden; }
  body {
    position: relative;
    font-family: "Arimo", Helvetica, Arial, sans-serif;
    color: var(--ink);
    background: #9a9a9a;
  }
  .backdrop {
    position: absolute; left: 206px; top: 0; width: 994px; height: 675px;
    background:
      radial-gradient(ellipse 300px 320px at 380px 380px, #c9c9c9 0%, rgba(170,170,170,0) 70%),
      radial-gradient(ellipse 220px 150px at 340px 100px, #dedede 0%, rgba(200,200,200,0) 75%),
      radial-gradient(ellipse 200px 260px at 860px 430px, #e4e4e4 0%, rgba(210,210,210,0) 70%),
      linear-gradient(135deg, #bdbdbd 0%, #a8a8a8 45%, #b9b9b9 100%);
  }
  .sidebar {
    position: absolute; left: 0; top: 0; width: 206px; height: 675px;
    background: var(--sidebar-bg);
    box-shadow: 3px 0 8px rgba(0,0,0,0.35);
    z-index: 2;
  }
  .brand {
    position: absolute; left: 18px; top: 36px; width: 180px;
    color: var(--plum); font-weight: 700; font-size: 25px; line-height: 31px;
  }
  .main-nav { position: absolute; left: 0; top: 139px; width: 206px; list-style: none; }
  .main-nav li a {
    display: block; height: 36.6px; line-height: 36.6px; padding-left: 19px;
    font-size: 12.5px; font-weight: 700; color: #fff; text-decoration: none;
  }
  .nav-portfolio a { background: var(--plum-dark); }
  .nav-about a { background: var(--plum); }
  .nav-blog a { background: var(--slate); }
  .nav-contact a { background: var(--sage); }
  .nav-lang a { background: var(--cream); color: var(--ink) !important; font-size: 10.5px !important; }
  .teaser {
    position: absolute; left: 18px; top: 368px; width: 170px;
    font-size: 11.6px; line-height: 15.2px; color: var(--muted-ink); letter-spacing: 0.2px;
  }
  .teaser-photo {
    float: left; width: 75px; height: 98px; margin: 0 9px 2px 1px;
    background: linear-gradient(160deg, #c9b48a 0%, #6c8a4a 45%, #3c5a2e 70%, #8a5c6a 100%);
  }
  .read-more { position: absolute; left: 103px; top: 539px; width: 85px; height: 23px; }
  .read-more span {
    position: absolute; left: 0; top: 0; width: 85px; line-height: 23px; text-align: center;
    font-family: "Dancing Script", cursive; font-size: 13px; color: #fff;
  }
  .social {
    position: absolute; left: 19px; top: 615px; list-style: none; display: flex; gap: 6px;
    font-size: 9px; color: var(--slate);
  }
  .copyright {
    position: absolute; left: 19px; top: 641px; font-size: 9.8px; font-weight: 700; color: var(--slate);
  }
  .about-panel {
    position: absolute; left: 455px; top: 169px; width: 497px; height: 337px;
    background: var(--panel-bg); border: 1px solid var(--panel-border);
    padding: 19px 19px 0 19px; z-index: 1;
  }
  .about-panel h1 {
    font-family: "Dancing Script", cursive; font-weight: 600; font-size: 26px;
    color: var(--plum-dark); line-height: 30px; margin-bottom: 12px;
  }
  .about-panel p { font-size: 12.2px; line-height: 17.8px; letter-spacing: 0.1px; }
  .portrait {
    float: left; width: 141px; height: 184px; margin: 0 15px 2px 1px;
    background: linear-gradient(170deg, #d8d4d0 0%, #8f8790 40%, #3b3437 65%, #6e8e56 100%);
  }
</style>
</head>
<body>
  <div class="backdrop" role="img" aria-label="Softened grey photograph of a glass bowl with large leaves and a white orchid on textured plaster"></div>

  <aside class="sidebar">
    <div class="brand">Maelis's<br>Spacial Design</div>
    <ul class="main-nav">
      <li class="nav-portfolio"><a href="#">Portfolio</a></li>
      <li class="nav-about"><a href="#">About Maelis</a></li>
      <li class="nav-blog"><a href="#">Blog</a></li>
      <li class="nav-contact"><a href="#">Contact Her</a></li>
      <li class="nav-lang"><a href="#">EN / CH</a></li>
    </ul>
    <div class="teaser">
      <div class="teaser-photo" role="img" aria-label="Photo of a floral table arrangement"></div>
      Lorem ipsum dolor sit amet, consecte adipiscing elit. Nunc ac quam eu quam euismod place. Donec a odio a lacus ullamer vestibulum. Proin id lorem sed velit feugiat sollicitudin. Ut sollicitudin congue mauris.
    </div>
    <a class="read-more" href="#">
      <svg width="85" height="23" viewBox="0 0 85 23"><polygon points="0,0 85,0 79,11.5 85,23 0,23 6,11.5" fill="#221427"/></svg>
      <span>Read More.</span>
    </a>
    <ul class="social">
      <li>chatnest</li><li>worklinq On</li><li>v+</li><li>xunmo</li>
    </ul>
    <p class="copyright">©2013 Maelis's Spacial Design.</p>
  </aside>

  <section class="about-panel">
    <h1>About Maelis</h1>
    <div class="portrait" role="img" aria-label="Photo of Maelis arranging white lilies in her studio"></div>
    <p>Lorem ipsum dolor sit amet, consectetur adipiscing elit. Sed nunc turpis, cursus nec molestie at, suscipit vitae nisi. Integer accumsan feugiat suscit. Morbi elit tellus, interdum nec elementum a, mollis ut eros. Morbi eu nisi leo. Aliquam gravida ultricies fermetum. Vestibulum vulputate laoreet purus vel semper. Cras luctus mollis ante eget venenatis. Proin ipsum dolor, condimentum a varius volutpat, rutrum eu dolor. Donec nec hendrerit erat. Donec arcu velit, laoreet suscipit lacinia non, fringilla at metus. Pellentesque non bibendum justo. Curabiur venenatis rutrum justo. Maecenas dui erat, laoreet ut consequat a, coiment nec lacus. Nam elementum venenatis odio. Sed est diam, semper a porta non, vulputate id ligula. In et diam enim, vitae sodales purus augue dolor sollicitudin id tempus a, euismod vitae.</p>
  </section>
</body>
</html>
```